White Cane Law Awareness Poster

Bright Harbor is a disability advocacy organization in Indiana. We are working on a project with the Cedarbrook Society of Staff for Low Sight. Our organizations need a design for a poster to promote awareness of Indiana's White Cane law. This poster will be displayed in local libraries, businesses, and other public places.

The poster should catch people's attention, and briefly explain that drivers have to yield for pedestrians who are blind who have white canes or seeing eye dogs.

The poster should be designed with people with low vision in mind. This means large text in a clear font, with good contrast between the text and the background. The text should be in a sans serif font that is clear and easy to read, with no italics or script fonts. There should not be a "busy" picture or pattern behind the text.

The poster should also include a reference to the relevant laws. We have attached a document with those references.

Finally, the poster should include the logos of Bright Harbor and the Cedarbrook Society of Staff for Low Sight, which we have included as attachments.

We have also included an attachment with a photo of the old White Cane Law poster, just to show an example of what we DO NOT want.

Industry/Entity Type

Non-Profit

Font styles to use
Sans Serif

Requirements
Must have
• The poster should also include a reference to the relevant laws. We have attached a document with those references.
• Finally, the poster should include the logos of Bright Harbor and the Cedarbrook Society of Staff for Low Sight, which we have included as attachments.

```html
<!DOCTYPE html>
<html lang="en">
<head>
<meta charset="utf-8">
<title>Indiana White Cane Law</title>
<link rel="stylesheet" href="https://fonts.googleapis.com/css2?family=Luckiest+Guy&display=swap">
<style>
  :root {
    --poster-yellow: #f5c816;
    --ink: #111111;
    --alert-red: #e30613;
    --sign-yellow: #fff200;
    --paper: #ffffff;
    --harbor-blue: #2b4fb8;
  }
  * { box-sizing: border-box; margin: 0; padding: 0; }
  html, body { width: 850px; height: 1200px; overflow: hidden; }
  body {
    background: var(--poster-yellow);
    font-family: "Luckiest Guy", "Arial Black", sans-serif;
    font-weight: 400;
    text-transform: uppercase;
    color: var(--ink);
    position: relative;
  }
  .poster-frame {
    position: absolute;
    left: 17px; top: 17px; width: 816px; height: 1166px;
    border: 6px solid var(--ink);
    border-radius: 36px;
  }
  .stop-sign {
    position: absolute;
    left: 222px; top: 56px; width: 406px; height: 414px;
  }
  .stop-word {
    font-family: "Luckiest Guy", "Arial Black", sans-serif;
    font-size: 124px;
    fill: var(--sign-yellow);
    stroke: var(--ink);
    stroke-width: 6px;
    paint-order: stroke;
  }
  .notice-box {
    position: absolute;
    left: 60px; width: 730px;
    background: var(--paper);
    border: 5px solid var(--ink);
    border-radius: 18px;
    text-align: center;
    white-space: nowrap;
    overflow: hidden;
  }
  .law-box { top: 484px; height: 246px; }
  .penalty-box { top: 732px; height: 186px; }
  .box-title {
    color: var(--alert-red);
    font-size: 54px;
    line-height: 1;
    font-weight: 400;
  }
  .law-box .box-title { margin-top: 22px; }
  .penalty-box .box-title { margin-top: 10px; }
  .citation {
    font-size: 13px;
    line-height: 1;
    margin-top: 14px;
  }
  .statute {
    font-size: 21px;
    line-height: 1.45;
    margin-top: 14px;
  }
  .flag { color: var(--alert-red); }
  .partner-society {
    position: absolute;
    left: 80px; top: 960px; width: 300px; height: 120px;
    display: flex; align-items: center; gap: 14px;
  }
  .partner-mark {
    flex: none;
    width: 26px; height: 26px;
    border-radius: 50%;
    background: var(--ink);
  }
  .partner-society .partner-name {
    font-size: 22px; line-height: 1.2; text-align: center;
  }
  .chapter-name {
    position: absolute;
    left: 48px; top: 1110px; width: 340px;
    text-align: center;
    font-size: 28px;
    line-height: 1;
  }
  .partner-harbor {
    position: absolute;
    left: 430px; top: 1080px; width: 370px;
    text-align: center;
    font-size: 44px; line-height: 1;
    color: var(--harbor-blue);
  }
</style>
</head>
<body>
  <div class="poster-frame" aria-hidden="true"></div>

  <svg class="stop-sign" viewBox="0 0 406 414" role="img" aria-label="Stop sign">
    <polygon points="119,4 287,4 402,121 402,293 287,410 119,410 4,293 4,121" fill="var(--ink)"/>
    <polygon points="122,12 284,12 394,124 394,290 284,402 122,402 12,290 12,124" fill="var(--paper)"/>
    <polygon points="128,26 278,26 380,130 380,284 278,388 128,388 26,284 26,130" fill="var(--ink)"/>
    <polygon points="130,31 276,31 375,132 375,282 276,383 130,383 31,282 31,132" fill="var(--alert-red)"/>
    <text class="stop-word" x="203" y="254" text-anchor="middle">STOP</text>
  </svg>

  <section class="notice-box law-box">
    <h1 class="box-title">Indiana White Cane Law</h1>
    <p class="citation">Ind. Code § 9-21-17-21 : Indiana Code - Section 9-21-17-21: Blind Pedestrians; Yield of Right-of-Way</p>
    <p class="statute">A person who drives a vehicle shall yield<br>
      the right-of-way to a blind pedestrian carrying a clearly<br>
      visible white cane or accompanied by a guide dog.</p>
  </section>

  <section class="notice-box penalty-box">
    <h2 class="box-title">Penalty</h2>
    <p class="citation">Ind. Code § 9-21-17-24 : Indiana Code - Section 9-21-17-24: Violations; <span class="flag">Class C Infraction</span></p>
    <p class="statute">A person who violates this chapter commits<br>
      a class C infraction. <span class="flag">(Misdemeanor)</span></p>
  </section>

  <div class="partner-society">
    <span class="partner-mark" aria-hidden="true"></span>
    <span class="partner-name">Cedarbrook Society of<br>Staff for Low Sight</span>
  </div>
  <p class="chapter-name">Fort Wayne Chapter</p>

  <p class="partner-harbor">Bright Harbor</p>
</body>
</html>
```